NOTE: I PROVIDED THE INCORRECT LOGO AND ONLY A HANDFUL OF PEOPLE NOTICED THAT IT WAS NOT THE ONE I DESCRIBED. THE LOGO I HAVE NOW ATTACHED MATCHES MY WEBSITE AND THE COLORS ON THE WEBSITE SHOULD BE USED FOR THE CARD.

PLEASE READ THE BUSINESS CARD DETAILS AND PROJECT MUST HAVES CAREFULLY.

I am looking for a business card that is powerful, a bit edgy, and although I work in the corporate world, not too formal. I would like to see designs that use the colors on my website www.brightlumo.com. I don't want the card to look washed out so please use shades of those colors that make them "pop". The "vibe" of the card needs to show substance and confidence while also reflecting that we're not your usual consultants.

The focus of my work is turning "people problems" into profits. Those problems could be poor service, an unstable workforce, untrained leaders, or managing change. We are an aggressive, results-focused team of performance improvement professionals who refuse to believe "things can't be done". For us, failure is not an option. Our logo reflects a target from the view of the site on a gun.

In addition to the contact information provided on the sample business card (do not include "turning people problems into profits"), I would like to include this statement (probably on the back):
I equip results-oriented business leaders to turn their people problems into profits in six months or less.

PLEASE NOTE THAT MY WEBSITE IS UNDER REVISION TO TONE DOWN THE MILITARY THEME, ALTHOUGH THE WARRIOR ENERGY AND FOCUS ON RESULTS REMAINS.

Target Market(s)

My clients are Mid and senior-level managers. I don't target any particular industry.

Industry/Entity Type

Consulting

Contact Information for Business Card

In addition to the contact information provided on the sample business card (DO NOT INCLUDE "turning people problems into profits"), I would like to include this statement (probably on the back):

I don't care whether the card is landscape or portrait view.

Font styles to use
Sans Serif

Requirements
Must have
• 1. be easy to read, no 6-8 point fonts!
• 2. a "vibe" that captures the eye without being too chaotic or busy
• 3. bold color, not washed out or boring - a good blend with the colors currently on my website (black, red, white, army green) but you don't need to use all of them.
• 4. all the contact information I have provided
• 5. a good blend with the colors currently on my website
• 6. Must have this quote on the back of the card: I equip results-oriented business leaders to turn their people problems into profits in six months or less.
Nice to have
• In looking at the sample images I provided for ideas, you can see that I like the way a card carries over from one side to the next.
• It would be great to find some aspect/quality/feature that I haven't seen before
Should not have
• 1. NO use of ALL CAPS
• 2. fonts that I would have to seek out and purchase (you should provide files for font if using something not standard)

```html
<!DOCTYPE html>
<html lang="en">
<head>
<meta charset="utf-8">
<title>Brightlumo Partners business card</title>
<link rel="stylesheet" href="https://fonts.googleapis.com/css2?family=Archivo:wght@700;800&family=Open+Sans:wght@400;600&display=swap">
<style>
  :root{
    --army:#6b7356;
    --army-dark:#5a6147;
    --signal-red:#e0533f;
    --ink:#3a3a36;
    --paper:#fbfbfa;
    --paper-edge:#e9e9e6;
    --night:#1d1d1f;
    --night-soft:#333336;
    --stage:#d9d6cf;
  }
  *{box-sizing:border-box;margin:0;padding:0}
  html,body{width:1200px;height:942px;overflow:hidden;background:var(--stage)}
  .stage{position:relative;width:1200px;height:942px;display:flex;flex-direction:column;align-items:center;justify-content:center;gap:56px}
  .card{position:relative;width:640px;height:366px;border-radius:4px;overflow:hidden;box-shadow:0 10px 28px rgba(0,0,0,.25)}

  /* Front */
  .card--front{background:radial-gradient(ellipse at 60% 45%,#ffffff 0%,var(--paper) 55%,var(--paper-edge) 100%);font-family:"Open Sans",sans-serif;color:var(--ink)}
  .contact{position:absolute;display:flex;flex-direction:column;gap:10px;font-size:15px}
  .contact--top{left:34px;top:30px}
  .contact--bottom{right:34px;bottom:30px;align-items:flex-end}
  .contact__row{display:flex;align-items:center;gap:10px}
  .contact--bottom .contact__row{flex-direction:row-reverse}
  .contact__row svg{width:18px;height:18px;flex:none}
  .identity{position:absolute;left:190px;top:96px;display:flex;flex-direction:column;align-items:flex-start}
  .brand{display:flex;align-items:center;gap:10px;font-family:"Archivo",sans-serif;font-weight:800;color:var(--army);font-size:26px;line-height:1}
  .brand__dot{width:16px;height:16px;border-radius:50%;background:var(--army)}
  .person{margin-top:26px;font-family:"Archivo",sans-serif;font-weight:800;font-size:30px;color:var(--army-dark);line-height:1}
  .role{margin-top:6px;font-size:16px;color:var(--signal-red)}
  .rule{margin-top:14px;width:84px;height:3px;background:var(--army)}

  /* Back */
  .card--back{background:linear-gradient(150deg,var(--night-soft) 0%,var(--night) 55%,#141415 100%)}
  .crosshair{position:absolute;left:0;right:0;top:150px;height:3px}
  .crosshair__left{position:absolute;left:0;width:90px;height:3px;background:var(--signal-red)}
  .crosshair__right{position:absolute;right:0;width:120px;height:3px;top:96px;background:var(--signal-red)}
  .back-brand{position:absolute;left:118px;top:98px;display:flex;align-items:center;gap:14px;font-family:"Archivo",sans-serif;font-weight:800;color:var(--army);font-size:42px;line-height:1}
  .back-brand__dot{width:26px;height:26px;border-radius:50%;background:var(--army)}
  .pledge{position:absolute;left:118px;top:180px;width:420px;font-family:"Archivo",sans-serif;font-weight:700;font-size:15px;line-height:1.45;color:var(--army)}
</style>
</head>
<body>
<main class="stage">

  <section class="card card--front" aria-label="Business card front">
    <div class="contact contact--top">
      <div class="contact__row">
        <svg viewBox="0 0 18 18" aria-hidden="true"><rect x="5" y="1.5" width="8" height="15" rx="1.5" fill="none" stroke="var(--signal-red)" stroke-width="1.6"/><circle cx="9" cy="13.5" r="1" fill="var(--signal-red)"/></svg>
        <span>555-203-4417</span>
      </div>
      <div class="contact__row">
        <svg viewBox="0 0 18 18" aria-hidden="true"><rect x="1.5" y="4" width="15" height="10" fill="var(--signal-red)"/><path d="M1.5 4 L9 10 L16.5 4" fill="none" stroke="#fff" stroke-width="1.3"/></svg>
        <span>danaw@brightlumo.com</span>
      </div>
    </div>

    <div class="identity">
      <div class="brand"><span class="brand__dot"></span>Brightlumo Partners</div>
      <div class="person">Dana Whitfield</div>
      <div class="role">Chief Performance Strategist</div>
      <div class="rule"></div>
    </div>

    <div class="contact contact--bottom">
      <div class="contact__row">
        <svg viewBox="0 0 18 18" aria-hidden="true"><path d="M2 7 Q9 1 16 7 L14 9 L12 7.5 L6 7.5 L4 9 Z" fill="var(--signal-red)"/><rect x="4.5" y="9.5" width="9" height="6" rx="1" fill="var(--signal-red)"/><circle cx="9" cy="12.5" r="1.6" fill="#fff"/></svg>
        <span>555-301-8826</span>
      </div>
      <div class="contact__row">
        <svg viewBox="0 0 18 18" aria-hidden="true"><g fill="none" stroke="var(--signal-red)" stroke-width="1.3"><circle cx="9" cy="9" r="7"/><ellipse cx="9" cy="9" rx="3" ry="7"/><path d="M2 9 H16 M3.5 5 H14.5 M3.5 13 H14.5"/></g></svg>
        <span>www.brightlumo.com</span>
      </div>
    </div>
  </section>

  <section class="card card--back" aria-label="Business card back">
    <div class="crosshair">
      <span class="crosshair__left"></span>
      <span class="crosshair__right"></span>
    </div>
    <div class="back-brand"><span class="back-brand__dot"></span>Brightlumo Partners</div>
    <p class="pledge">I equip results-oriented business leaders to turn their people problems into profits in six months or less.</p>
  </section>

</main>
</body>
</html>
```